Video Company website for high tech video software company

Design a website for a software company that has an extensive list of products that process incoming TV video and video ads and processes the video for delivery to mobile phones, tablets, Set Top Boxes, and PCs.

Coding

Coded - Design and coding required

Number of Pages Required

1 page

```html
<!DOCTYPE html>
<html lang="en">
<head>
<meta charset="utf-8">
<title>Beamline TV — High Quality Transcoding</title>
<link rel="stylesheet" href="https://fonts.googleapis.com/css2?family=Outfit:wght@400;500;600&display=swap">
<style>
:root{
  --black:#000;
  --ink:#fff;
  --teal:#2bd0d8;
  --blue:#0096d9;
  --dark:#1d1d1e;
  --footer:#252526;
  --muted:#c9c9c9;
  --purple-1:#1b0f4a;
  --purple-2:#3a136b;
  --purple-3:#5a1670;
}
*{margin:0;padding:0;box-sizing:border-box}
html,body{width:926px;height:1200px;overflow:hidden;background:var(--dark)}
body{position:relative;font-family:"Outfit",sans-serif;color:var(--ink)}
.site-header{position:absolute;left:0;top:0;width:926px;height:50px;background:var(--black)}
.brand{position:absolute;display:flex;align-items:center;gap:5px;font-weight:600;color:var(--ink);white-space:nowrap}
.brand-mark{width:12px;height:12px;border-radius:50%;background:var(--blue)}
.site-header .brand{left:122px;top:15px;font-size:17px}
.main-nav{position:absolute;top:18px;right:123px;display:flex;gap:17px;font-size:11px;font-weight:500}
.main-nav a,.footer-nav a{color:var(--ink);text-decoration:none}

.hero{position:absolute;left:0;top:50px;width:926px;height:298px;
  background:linear-gradient(100deg,var(--purple-1) 0%,var(--purple-2) 45%,var(--purple-3) 100%)}
.hero-visual{position:absolute;left:456px;top:0;width:382px;height:189px;
  background:radial-gradient(ellipse at 50% 45%,rgba(120,60,170,.55) 0%,rgba(90,30,130,.25) 60%,rgba(90,30,130,0) 100%)}
.hero-title{position:absolute;left:122px;top:104px;font-size:22px;font-weight:600;color:var(--teal);white-space:nowrap}
.hero-sub{position:absolute;left:123px;top:138px;font-size:12.5px;letter-spacing:2px;font-weight:400;white-space:nowrap}
.product-tabs{position:absolute;left:123px;top:186px;height:21px}
.tab{position:absolute;top:0;height:21px;border:1px solid var(--ink);border-radius:2px;font-size:9.5px;display:flex;align-items:center;justify-content:center;white-space:nowrap}
.tab.is-active{background:var(--blue);border-color:var(--blue)}
.tab.is-active::after{content:"";position:absolute;bottom:-5px;left:50%;margin-left:-4px;border-style:solid;border-color:var(--blue) transparent transparent;border-width:5px 4px 0}
.progress{position:absolute;left:123px;top:222px;width:497px;height:2px;background:linear-gradient(90deg,#fff,rgba(255,255,255,.35))}
.progress-knob{position:absolute;left:49px;top:-4px;width:10px;height:10px;border-radius:50%;background:var(--teal);box-shadow:0 0 0 2px rgba(43,208,216,.3)}
.format-badge{position:absolute;top:240px;height:26px;border-radius:2px}

.features{position:absolute;left:0;top:348px;width:926px;height:666px;
  background:radial-gradient(ellipse at 80% 30%,#2a2a2b 0%,var(--dark) 60%)}
.features-title{position:absolute;left:0;top:28px;width:926px;text-align:center;font-size:20.5px;font-weight:600;line-height:32px}
.card{position:absolute;width:159px;height:245px;background:var(--blue);padding:4px}
.card-media{width:151px;height:112px}
.card-list{list-style:none;margin-top:12px;text-align:center;font-size:11px;font-weight:500;line-height:22.2px;white-space:nowrap}

.site-footer{position:absolute;left:0;top:1014px;width:926px;height:186px;background:var(--footer)}
.site-footer .brand{left:50%;transform:translateX(-50%);top:33px;font-size:17px}
.footer-nav{position:absolute;top:72px;left:0;width:926px;display:flex;justify-content:center;gap:17px;font-size:11px;font-weight:500}
.social{position:absolute;top:101px;left:0;width:926px;display:flex;justify-content:center;gap:6px}
.social-link{width:28px;height:28px;border-radius:50%;background:var(--blue);display:block}
.copyright{position:absolute;top:151px;left:0;width:926px;text-align:center;font-size:9.5px;color:var(--muted)}
</style>
</head>
<body>

<header class="site-header">
  <div class="brand"><span>Beamline TV</span><span class="brand-mark"></span></div>
  <nav class="main-nav"><a href="#">Products</a><a href="#">Resources</a><a href="#">Contact</a></nav>
</header>

<section class="hero">
  <div class="hero-visual" role="img" aria-label="Network of connected devices: phones and a tablet linked by lines"></div>

  <h1 class="hero-title">High Quality Transcoding</h1>
  <p class="hero-sub">OTT IPTV DVB COMPLETE SOLUTION</p>

  <div class="product-tabs">
    <span class="tab is-active" style="left:0;width:107px">Ingested Transcoding</span>
    <span class="tab" style="left:112px;width:65px">Middleware</span>
    <span class="tab" style="left:183px;width:120px">Subscriber Management</span>
    <span class="tab" style="left:309px;width:50px">Security</span>
    <span class="tab" style="left:364px;width:59px">Streaming</span>
    <span class="tab" style="left:429px;width:29px">Ads</span>
    <span class="tab" style="left:464px;width:37px">Apps</span>
  </div>
  <div class="progress"><span class="progress-knob"></span></div>

  <span class="format-badge" style="left:123px;width:34px;background:#2a2a2a"></span>
  <span class="format-badge" style="left:167px;width:34px;background:#e8a51a"></span>
  <span class="format-badge" style="left:211px;width:31px;background:#c9a02a"></span>
  <span class="format-badge" style="left:252px;width:34px;background:#c9a02a"></span>
  <span class="format-badge" style="left:297px;width:48px;background:#e2e2e2"></span>
</section>

<section class="features">
  <h2 class="features-title">High Quality High Density 150 channels<br>in 1RU 24/7 Reliability Error Analysis</h2>

  <article class="card" style="left:123px;top:119px">
    <div class="card-media" role="img" aria-label="Viewer browsing a streaming TV interface" style="background:linear-gradient(160deg,#3a3f48,#9a6b3a 60%,#d9d6d0)"></div>
    <ul class="card-list"><li>OTT / IPTV APPs</li><li>Live TV</li><li>Catchup TV</li><li>VOD</li><li>Recommendations</li></ul>
  </article>
  <article class="card" style="left:297px;top:119px">
    <div class="card-media" role="img" aria-label="Hand holding a glowing cloud symbol" style="background:linear-gradient(160deg,#0d1a3a,#3a2d5a 55%,#8a2a3a)"></div>
    <ul class="card-list"><li>MSO Scale</li><li>Cloud option</li><li>Nationwide Distribution</li><li>Individual lineups</li><li>Shared infrastructure</li></ul>
  </article>
  <article class="card" style="left:470px;top:119px">
    <div class="card-media" role="img" aria-label="Person with a megaphone holding a tablet" style="background:linear-gradient(120deg,#1a2a4a,#5a2a3a 50%,#d9a020)"></div>
    <ul class="card-list"><li>Advertising</li><li>Targeted Advertising</li><li>Regional</li><li>Addressable ads</li><li>Ad analytics</li></ul>
  </article>
  <article class="card" style="left:644px;top:119px">
    <div class="card-media" role="img" aria-label="Glowing security shield with keyhole" style="background:radial-gradient(circle,#22c8ef 0%,#1a4ad0 50%,#1a1a9a 100%)"></div>
    <ul class="card-list"><li>CAS / DRM</li><li>Hollywood approved</li><li>Highly secure</li><li>CAS and DRM systems</li></ul>
  </article>

  <article class="card" style="left:123px;top:379px">
    <div class="card-media" role="img" aria-label="Presenter at a desk in a lit studio" style="background:linear-gradient(120deg,#b55a10,#f08a1a 55%,#5a2a10)"></div>
    <ul class="card-list"><li>High Capacity Streaming</li><li>Edge Cache</li><li>Cloud managed</li><li>No 3rd party CDN needed</li></ul>
  </article>
  <article class="card" style="left:297px;top:379px">
    <div class="card-media" role="img" aria-label="Pile of red play buttons" style="background:linear-gradient(140deg,#c01818,#e83030 50%,#8a1010)"></div>
    <ul class="card-list"><li>Subscriber</li><li>Management</li><li>System</li></ul>
  </article>
  <article class="card" style="left:470px;top:379px">
    <div class="card-media" role="img" aria-label="Red cube frame among clouds" style="background:linear-gradient(140deg,#3a4048,#8a9098 55%,#d8dadc)"></div>
    <ul class="card-list"><li>Transcoding</li><li>High Quality</li><li>High Density</li></ul>
  </article>
  <article class="card" style="left:644px;top:379px">
    <div class="card-media" role="img" aria-label="Viewer watching on-demand content on a TV" style="background:linear-gradient(150deg,#2a3a4a,#4a6a7a 55%,#c8c4be)"></div>
    <ul class="card-list"><li>VOD</li><li>CDN</li><li>Content Ingest</li><li>Catchup TV</li></ul>
  </article>
</section>

<footer class="site-footer">
  <div class="brand"><span>Beamline TV</span><span class="brand-mark"></span></div>
  <nav class="footer-nav"><a href="#">Products</a><a href="#">Resources</a><a href="#">Contact</a></nav>
  <div class="social">
    <a class="social-link" href="#" aria-label="Social profile 1"></a>
    <a class="social-link" href="#" aria-label="Social profile 2"></a>
    <a class="social-link" href="#" aria-label="Social profile 3"></a>
  </div>
  <p class="copyright">Copyright © 2021 Beamline TV. All rights reserved.</p>
</footer>

</body>
</html>
```